Security Warning Sign

We have an existing sign that needs an update. I have attached a picture of the current square sign. We need to maintain the same wording. It needs to be professional and appropriate to attach to our customers fence. Also attached is a copy of our building sign which may lend some inspiration and hopefully the ai format will assist. The final sign will be 600mm x 600mmOur website is www.harbourlinewatch.com.au

```html
<!DOCTYPE html>
<html lang="en">
<head>
<meta charset="utf-8">
<title>Security Warning Sign</title>
<link href="https://fonts.googleapis.com/css2?family=Anton&family=Jost:wght@700&display=swap" rel="stylesheet">
<style>
  :root {
    --orange: #f28532;
    --charcoal: #2f2f2f;
    --ink: #1c1c1c;
    --white: #ffffff;
    --paper-shade: #ececec;
  }
  html, body {
    margin: 0;
    padding: 0;
    width: 1200px;
    height: 1200px;
    overflow: hidden;
    background: var(--white);
  }
  .sign {
    position: relative;
    width: 1200px;
    height: 1200px;
    background: linear-gradient(135deg, var(--white) 0%, #f7f7f7 45%, var(--paper-shade) 100%);
    overflow: hidden;
  }
  .sign-title {
    position: absolute;
    top: 60px;
    left: 0;
    width: 1200px;
    margin: 0;
    text-align: center;
    font-family: "Anton", "Impact", sans-serif;
    font-weight: 400;
    font-size: 296px;
    line-height: 1;
    letter-spacing: 2px;
    color: var(--orange);
  }
  .notice-band {
    position: absolute;
    top: 370px;
    left: 0;
    width: 1200px;
    height: 596px;
    background: var(--charcoal);
    display: flex;
    align-items: center;
    justify-content: center;
  }
  .notice-text {
    margin: 0;
    text-align: center;
    font-family: "Jost", "Futura", sans-serif;
    font-weight: 700;
    font-size: 94px;
    line-height: 100px;
    color: var(--white);
  }
  .footer {
    position: absolute;
    top: 966px;
    left: 0;
    width: 1200px;
    height: 234px;
  }
  .brand {
    position: absolute;
    left: 95px;
    top: 50px;
    display: flex;
    align-items: center;
    gap: 22px;
  }
  .brand-dot {
    width: 130px;
    height: 130px;
    border-radius: 50%;
    background: var(--orange);
    flex: none;
  }
  .brand-name {
    font-family: "Jost", "Futura", sans-serif;
    font-weight: 700;
    font-size: 38px;
    line-height: 38px;
    color: var(--ink);
    text-transform: uppercase;
  }
  .phone {
    position: absolute;
    right: 48px;
    top: 62px;
    font-family: "Anton", "Impact", sans-serif;
    font-size: 104px;
    line-height: 1;
    color: var(--orange);
    letter-spacing: 1px;
  }
</style>
</head>
<body>
  <main class="sign">
    <h1 class="sign-title">WARNING</h1>
    <section class="notice-band">
      <p class="notice-text">ELECTRONIC<br>SURVEILLANCE AND<br>RECORDING<br>DEVICES INSTALLED<br>IN THIS AREA</p>
    </section>
    <footer class="footer">
      <div class="brand">
        <span class="brand-dot"></span>
        <span class="brand-name">Harbourline<br>Watch<br>Services</span>
      </div>
      <div class="phone">1300 555 018</div>
    </footer>
  </main>
</body>
</html>
```